Asian Speciality Coffee label for brown valve bag. YUNNAN.

We are in need of a front and back coffee label for a brown paper valve bag.

Our brand is Lumo Brava. We source the finest and rarest varieties of coffee from the four corners of South East Asia that have been until now kept secret. Our selection has been cultivated by tribal communities and micro lot farmers who for generations have taken pride in organically producing truly amazing coffees. The result is coffee unlike any we have ever tasted before, truly showing how special Asian kapé can be. We believe every bean is precious which is why we ensure all our coffees are sourced ethically through direct trade, roasted by specialists and treated with utmost respect to fulfill our promise of serving you kapé that gives happiness in every cup.

The design of the label will encompass our Company Name logo and signature drinking buddha logo. We want a logo that stands out but at the sane time clearly displaying the finer details of the coffee, such as taste notes, variety etc.

The particular variety we want a label for is called YUNNAN.
Complete details of the coffee are found on our websitehttp://www.lumobrava-example.com/shop/yunnan

The front of the bag I would ideally like a picture of the farmer, of which I have provided on website or attached. Together with the name of the coffee and our company logo. Perhaps further details of the coffee can be found on the back. But would like to see creative input.

please look up our website to read more about us. www.lumobrava-example.com

Target Market(s)

Speciality Coffee

Requirements
Must have
• Company name logo Lumo Brava, Drinking Buddha stamp. Details about the coffee. Product name: Yunnan.
• Product details can be found here http://www.lumobrava-example.com/shop/yunnan
• or
• Origin: Yunnan Province, Southern China
• Variety: Arabica - Catimor
• Altitude Grown: 1100 - 1400 ft
• Farmer: Co-operative of micro lots
• Process: Fully Washed
• Yunnan’, in local dialect means ‘South of the Cloud’. The Yunnan province located in Southern China is graced with world renowned scenic beauty for its tranquil mountainous valleys. The name we chose for this coffee originated from the location of the coffee trees growing south of the Yunling Mountains (known to locals as Cloud Mountain).Our ‘Yunnan’ coffee is grown south of the Yunling in the rolling hills of Bao Shan and Kunming at an altitude of 1100 - 1400 meters. Pairing organic farming methods and top grade washing and sorting facilities have allowed the farms we work with to perfect their coffee to specialty grade quality. The result of their hard work and dedication to their harvest was evident to us from our first cup.
Should not have
• sticker label will be on a brown paper bag.

```html
<!DOCTYPE html>
<html lang="en">
<head>
<meta charset="utf-8">
<title>Lumo Brava – Yunnan coffee label</title>
<link href="https://fonts.googleapis.com/css2?family=Playfair+Display:wght@700;900&family=Oswald:wght@500&family=Roboto+Condensed:wght@400;700&display=swap" rel="stylesheet">
<style>
  :root {
    --backdrop: #2a1810;
    --bag-amber: #d9914a;
    --bag-cream: #f2cf9c;
    --bag-brown: #7a3d1c;
    --label-red: #b3161c;
    --label-red-dark: #7e0d12;
    --gold: #e8b84a;
    --gold-dark: #a8741c;
    --paper: #f4efe6;
    --ink: #2b1a10;
    --text-light: #fff8ee;
  }
  * { box-sizing: border-box; margin: 0; padding: 0; }
  html, body { width: 1200px; height: 1164px; overflow: hidden; background: var(--backdrop); }
  .canvas { position: relative; width: 1200px; height: 1164px; }

  .side-panel {
    position: absolute; left: 190px; top: 40px; width: 170px; height: 1084px;
    background: linear-gradient(180deg, #8a4a22, #5a2c14);
    padding: 150px 14px 20px;
  }
  .side-panel .side-brand {
    background: var(--label-red); color: var(--text-light);
    font: 500 20px/1 "Oswald", sans-serif; text-align: center; padding: 14px 4px; margin-bottom: 40px;
  }
  .spec-card, .story-card {
    background: rgba(244, 228, 200, 0.88); color: var(--ink);
    font: 400 11px/1.4 "Roboto Condensed", sans-serif; padding: 10px; margin-bottom: 16px;
  }
  .spec-card b { font-weight: 700; }
  .story-card { font-size: 10.5px; }

  .front-panel {
    position: absolute; left: 370px; top: 40px; width: 600px; height: 1084px; overflow: hidden;
  }
  .front-art {
    position: absolute; inset: 0;
    background: radial-gradient(circle at 75% 40%, var(--bag-brown), transparent 45%),
                radial-gradient(circle at 25% 30%, #a85a2c, transparent 40%),
                linear-gradient(180deg, var(--bag-cream), var(--bag-amber) 55%, #b86a30);
  }
  .stitch {
    position: absolute; left: 20px; right: 20px; top: 52px; border-top: 3px dotted var(--gold);
  }
  .brand-ribbon {
    position: absolute; left: 222px; top: 12px; width: 156px; height: 226px;
    background: linear-gradient(180deg, #c81c22, #8e1016);
    display: flex; align-items: center; justify-content: center;
  }
  .brand-name {
    color: var(--text-light); font: 500 30px/1.1 "Oswald", sans-serif; text-align: center;
  }
  .photo-frame {
    position: absolute; left: 80px; top: 570px; width: 470px; height: 500px;
    border: 8px solid var(--gold); box-shadow: inset 0 0 0 2px var(--gold-dark);
  }
  .farmer-photo {
    width: 100%; height: 100%;
    background: linear-gradient(180deg, #c9cdd0 0%, #e6d2a8 22%, #4a3a30 40%, #6b2a22 70%, #4e1414 100%);
  }
  .title-panel {
    position: absolute; left: 130px; top: 405px; width: 340px; height: 170px;
    background: linear-gradient(180deg, #c81c22, var(--label-red-dark));
    border: 4px solid var(--paper); border-radius: 14px;
    display: flex; flex-direction: column; align-items: center; justify-content: center;
    padding-bottom: 14px;
  }
  .since {
    color: var(--paper); font: 700 13px/1 "Playfair Display", serif; letter-spacing: 1px;
    margin-bottom: 6px;
  }
  .product-name {
    color: var(--text-light); font: 900 64px/1 "Playfair Display", serif; letter-spacing: 1px;
  }
  .quality-tag {
    position: absolute; left: 160px; top: 562px; width: 280px; height: 38px;
    background: var(--paper); border: 2px dashed #c9b8a0;
    color: var(--label-red); font: 700 16px/34px "Playfair Display", serif; text-align: center;
  }
  .buddha-stamp {
    position: absolute; left: 245px; top: 930px; width: 130px; height: 130px; border-radius: 50%;
    background: radial-gradient(circle, #ffd45a, #f0a818);
    border: 6px solid var(--gold-dark); box-shadow: 0 0 0 3px var(--gold);
  }
</style>
</head>
<body>
<div class="canvas">

  <aside class="side-panel">
    <div class="side-brand">YUNNAN</div>
    <div class="spec-card">
      <b>Origin:</b> Yunnan Province, Southern China<br>
      <b>Variety:</b> Arabica - Catimor<br>
      <b>Altitude Grown:</b> 1100 - 1400 ft<br>
      <b>Farmer:</b> Co-operative of micro lots<br>
      <b>Process:</b> Fully Washed
    </div>
    <div class="story-card">
      ‘Yunnan’, in local dialect means ‘South of the Cloud’. The Yunnan province located in Southern China is graced with world renowned scenic beauty for its tranquil mountainous valleys. The name we chose for this coffee originated from the location of the coffee trees growing south of the Yunling Mountains (known to locals as Cloud Mountain). Our ‘Yunnan’ coffee is grown south of the Yunling in the rolling hills of Bao Shan and Kunming at an altitude of 1100 - 1400 meters. Pairing organic farming methods and top grade washing and sorting facilities have allowed the farms we work with to perfect their coffee to specialty grade quality.
    </div>
  </aside>

  <section class="front-panel">
    <div class="front-art" role="img" aria-label="Close-up of roasted coffee beans with rising steam in warm amber tones"></div>
    <div class="stitch"></div>

    <div class="brand-ribbon"><div class="brand-name">Lumo Brava</div></div>

    <div class="photo-frame">
      <div class="farmer-photo" role="img" aria-label="Farmer raking red coffee cherries drying in the sun on a hillside"></div>
    </div>

    <div class="title-panel">
      <div class="since">SINCE 1900</div>
      <div class="product-name">YUNNAN</div>
    </div>
    <div class="quality-tag">PREMIUM QUALITY COFFEE</div>

    <div class="buddha-stamp" role="img" aria-label="Drinking Buddha stamp: seated figure sipping from a cup"></div>
  </section>

</div>
</body>
</html>
```